Corwin Crest Homes Needs Business Card Design

Looking for a unique modern business card to fit my new Logo.
Name: Marcus Corwin
Company: Corwin Crest Homes, LLC
Tag Line: Crafted With Care
Email: corwincresthomes@mailnest.example
Phone: (555) 017-2846
Website: www.corwincresthomes.example
License: CORWICH462KX

```html
<!DOCTYPE html>
<html lang="en">
<head>
<meta charset="utf-8">
<title>Corwin Crest Homes — Business Card</title>
<link href="https://fonts.googleapis.com/css2?family=Montserrat:wght@400;500;600;700;800&display=swap" rel="stylesheet">
<style>
  :root {
    --stage: #e9e6e1;
    --card-white: #ffffff;
    --brand-blue: #3596c9;
    --ink: #111111;
    --text: #333333;
    --faint: #ececec;
  }
  * { margin: 0; padding: 0; box-sizing: border-box; }
  html, body { width: 900px; height: 1200px; overflow: hidden; }
  body {
    background: var(--stage);
    font-family: "Montserrat", Arial, sans-serif;
    position: relative;
  }
  .card {
    position: absolute;
    left: 80px;
    width: 742px;
    height: 440px;
    border-radius: 30px;
    overflow: hidden;
    box-shadow: 0 6px 14px rgba(0,0,0,0.35);
  }
  .card-front { top: 132px; background: var(--card-white); }
  .card-back { top: 638px; background: var(--brand-blue); }

  .front-wordmark {
    position: absolute;
    left: 48px;
    top: 40px;
    display: flex;
    align-items: center;
    gap: 16px;
  }
  .wordmark-square {
    width: 66px; height: 66px;
    border: 5px solid var(--brand-blue);
    flex: none;
  }
  .wordmark-name {
    font-weight: 800;
    font-size: 30px;
    line-height: 1.05;
    letter-spacing: 0.5px;
    color: var(--ink);
    text-transform: uppercase;
  }
  .faint-square {
    position: absolute;
    left: 446px;
    top: 168px;
    width: 360px;
    height: 360px;
    border: 14px solid var(--faint);
  }

  .contact-block {
    position: absolute;
    left: 40px;
    top: 214px;
    color: var(--ink);
  }
  .person-name {
    font-size: 27px;
    font-weight: 700;
    color: var(--brand-blue);
    line-height: 1.1;
  }
  .person-title { font-size: 16px; font-weight: 500; margin-top: 4px; }
  .license { margin-top: 20px; font-size: 16px; color: var(--text); }
  .license-label { color: var(--brand-blue); font-weight: 600; }
  .contact-list { list-style: none; margin-top: 20px; }
  .contact-list li {
    display: flex; align-items: center; gap: 12px;
    font-size: 16px; color: var(--text); height: 25px;
  }
  .contact-list svg { width: 16px; height: 16px; fill: var(--brand-blue); flex: none; }

  .back-wordmark {
    position: absolute;
    left: 0; right: 0;
    top: 160px;
    display: flex;
    justify-content: center;
    align-items: center;
    gap: 22px;
  }
  .back-wordmark .wordmark-square { width: 110px; height: 110px; border: 7px solid #fff; }
  .back-wordmark .wordmark-name { color: #fff; font-size: 42px; }
  .tagline {
    position: absolute;
    left: 0; right: 0;
    top: 380px;
    text-align: center;
    color: #fff;
    font-size: 17px;
    font-weight: 500;
    letter-spacing: 4px;
  }
</style>
</head>
<body>
  <section class="card card-front">
    <div class="faint-square"></div>
    <div class="front-wordmark">
      <div class="wordmark-square"></div>
      <div class="wordmark-name">Corwin Crest<br>Homes</div>
    </div>
    <div class="contact-block">
      <h1 class="person-name">Marcus Corwin</h1>
      <p class="person-title">CEO &amp; Founder</p>
      <p class="license"><span class="license-label">License:</span> CORWICH462KX</p>
      <ul class="contact-list">
        <li><svg viewBox="0 0 16 16"><path d="M2 5c0-2 2-3 6-3s6 1 6 3v1h-3V5H5v1H2z M4 7h8l2 6H2z M8 8.5a2 2 0 1 0 0 4 2 2 0 0 0 0-4z"/></svg>(555) 017-2846</li>
        <li><svg viewBox="0 0 16 16"><path d="M1 4h14v1L8 9 1 5z M1 6.5l7 4 7-4V12H1z"/></svg>corwincresthomes@mailnest.example</li>
        <li><svg viewBox="0 0 16 16"><circle cx="8" cy="8" r="6.5"/><path d="M5 4c1 1 2 1 2 3s-2 1-2 3M10 6c1 0 2 1 1 3" stroke="#fff" stroke-width="1.2" fill="none"/></svg>www.corwincresthomes.example</li>
      </ul>
    </div>
  </section>

  <section class="card card-back">
    <div class="back-wordmark">
      <div class="wordmark-square"></div>
      <div class="wordmark-name">Corwin Crest<br>Homes</div>
    </div>
    <p class="tagline">Crafted With Care</p>
  </section>
</body>
</html>
```